Stationary Design for Norvath Digital

We are after a full stationary back business cards, letterheads, compliment slip, invoice template, delivery note and anything else we could use within the stationary pack.

We would also like an email footer creating.

Our company details to be included on all stationary:

Registered Name: Norvath Limited
Company Registration Number: 20473915
Website: www.norvathdigital.example
email: info@norvathdigital.example
Phone: 01632 960 417
Address: 48 Tamsin Lane Loughborough Leicestershire United Kingdom LE11 9QX

```html
<!DOCTYPE html>
<html lang="en">
<head>
<meta charset="utf-8">
<title>Norvath Digital – Stationery Pack</title>
<link rel="stylesheet" href="https://fonts.googleapis.com/css2?family=Michroma&family=Exo+2:wght@300;400&display=swap">
<style>
  :root {
    --backdrop: #e6e7ea;
    --paper: #ffffff;
    --band: #b9bdcc;
    --navy: #1d3a7a;
    --ink: #6f7487;
    --ink-on-band: #ffffff;
    --shadow: 0 2px 6px rgba(40, 45, 60, 0.12);
  }
  * { box-sizing: border-box; margin: 0; padding: 0; }
  html, body { width: 1200px; height: 800px; overflow: hidden; }
  body {
    background: var(--backdrop);
    font-family: "Exo 2", "Helvetica Neue", Arial, sans-serif;
    color: var(--ink);
    position: relative;
  }
  .sheet {
    position: absolute;
    background: var(--paper);
    box-shadow: var(--shadow);
    overflow: hidden;
  }
  .sheet > svg.curve {
    position: absolute; inset: 0; width: 100%; height: 100%;
  }
  .curve path { fill: var(--band); }
  .brand {
    position: absolute;
    font-family: "Michroma", "Arial", sans-serif;
    color: var(--navy);
    letter-spacing: 0.08em;
    display: flex; align-items: center; gap: 0.45em;
    white-space: nowrap;
  }
  .brand .dot {
    width: 0.55em; height: 0.55em; border-radius: 50%; background: currentColor;
  }
  .details {
    position: absolute;
    color: var(--ink-on-band);
    font-weight: 300;
    line-height: 1.5;
    white-space: nowrap;
  }
  .details .company {
    font-family: "Michroma", "Arial", sans-serif;
    letter-spacing: 0.08em;
    font-weight: 400;
    margin-bottom: 0.5em;
  }

  /* Letterhead */
  .letterhead { left: 40px; top: 40px; width: 500px; height: 720px; }
  .letterhead .brand { left: 44px; top: 48px; font-size: 22px; }
  .letterhead .details { right: 34px; bottom: 30px; text-align: right; font-size: 9px; }
  .letterhead .details .company { font-size: 13px; }

  /* Compliment slip */
  .compliment { left: 570px; top: 40px; width: 320px; height: 152px; }
  .compliment .brand { left: 20px; top: 24px; font-size: 14px; }
  .compliment .greeting {
    position: absolute; left: 20px; bottom: 22px;
    font-family: "Michroma", "Arial", sans-serif;
    font-size: 8.5px; letter-spacing: 0.12em; color: var(--ink);
    white-space: nowrap;
  }
  .compliment .details { right: 12px; top: 20px; text-align: right; font-size: 5px; }
  .compliment .details .company { font-size: 6px; }

  /* Notepad */
  .notepad { left: 570px; top: 222px; width: 320px; height: 538px; }
  .notepad .rings {
    position: absolute; left: 16px; right: 16px; top: 8px; height: 16px;
    display: flex; justify-content: space-between;
  }
  .notepad .rings span {
    width: 4px; height: 16px; border-radius: 2px; background: #9a9eab;
  }
  .notepad .faint-name {
    position: absolute; left: 30px; top: 70px;
    font-family: "Michroma", "Arial", sans-serif;
    font-size: 34px; letter-spacing: 0.06em; color: #eceef2;
  }
  .notepad .details { right: 24px; bottom: 24px; text-align: right; font-size: 7px; }
  .notepad .details .company { font-size: 11px; }

  /* Business cards */
  .card { top: 40px; width: 110px; height: 170px; }
  .card-front { left: 920px; }
  .card-back { left: 1050px; background: var(--band); }
  .card-front .brand { left: 12px; top: 16px; font-size: 10px; }
  .card-front .person {
    position: absolute; left: 12px; top: 62px; color: var(--ink-on-band);
    font-size: 5.5px; line-height: 1.5; font-weight: 300;
  }
  .card-front .person .name {
    font-family: "Michroma", "Arial", sans-serif; font-size: 7px; letter-spacing: 0.06em; font-weight: 400;
  }
  .card-front .person .role { margin-bottom: 6px; }
  .card-front .person .company {
    font-family: "Michroma", "Arial", sans-serif; font-size: 6px; letter-spacing: 0.06em; margin-bottom: 6px; font-weight: 400;
  }
  .card-back .brand {
    left: 50%; top: 50%; transform: translate(-50%, -50%);
    font-size: 10px; color: var(--ink-on-band);
  }

  /* Envelope */
  .envelope { left: 920px; top: 240px; width: 240px; height: 340px; }
  .envelope .brand {
    left: 22px; top: 110px; font-size: 16px; color: var(--ink-on-band);
  }
  .envelope .details { left: 16px; bottom: 16px; font-size: 5.5px; color: var(--ink); }
  .envelope .details .company { font-size: 8px; }

  /* Pens */
  .pen {
    position: absolute; left: 920px; width: 240px; height: 24px;
    border-radius: 12px 4px 4px 12px;
    background: var(--paper);
    box-shadow: var(--shadow);
  }
  .pen .grip {
    position: absolute; left: 46px; top: 0; width: 150px; height: 100%;
    background: var(--band);
    display: flex; align-items: center; justify-content: center;
    color: var(--ink-on-band);
    font-size: 7.5px; letter-spacing: 0.06em;
  }
  .pen .clip {
    position: absolute; left: 150px; top: -5px; width: 84px; height: 6px;
    border-radius: 3px; background: #d9dbe2;
  }
  .pen .tip {
    position: absolute; left: -8px; top: 9px; width: 10px; height: 6px;
    border-radius: 3px 0 0 3px; background: #9a9eab;
  }
</style>
</head>
<body>

  <!-- Letterhead -->
  <section class="sheet letterhead" aria-label="Letterhead">
    <svg class="curve" viewBox="0 0 100 100" preserveAspectRatio="none" aria-hidden="true">
      <path d="M0,100 L0,91 C40,90 78,72 100,34 L100,100 Z"/>
    </svg>
    <div class="brand"><span class="dot"></span>NORVATH</div>
    <div class="details">
      <div class="company">NORVATH LIMITED</div>
      <div>w: www.norvathdigital.example &nbsp;|&nbsp; e: info@norvathdigital.example &nbsp;|&nbsp; t: 01632 960 417</div>
      <div>48 Tamsin Lane Loughborough Leicestershire United Kingdom LE11 9QX</div>
      <div>Company Number: 20473915</div>
    </div>
  </section>

  <!-- Compliment slip -->
  <section class="sheet compliment" aria-label="Compliment slip">
    <svg class="curve" viewBox="0 0 100 100" preserveAspectRatio="none" aria-hidden="true">
      <path d="M100,0 L60,0 C56,40 64,75 58,100 L100,100 Z"/>
    </svg>
    <div class="brand"><span class="dot"></span>NORVATH</div>
    <div class="greeting">WITH COMPLIMENTS</div>
    <div class="details">
      <div class="company">NORVATH LIMITED</div>
      <div>w: www.norvathdigital.example</div>
      <div>e: info@norvathdigital.example</div>
      <div>t: 01632 960 417</div>
      <div>48 Tamsin Lane</div>
      <div>Loughborough, Leicestershire</div>
      <div>United Kingdom LE11 9QX</div>
      <div>Company Number: 20473915</div>
    </div>
  </section>

  <!-- Notepad -->
  <section class="sheet notepad" aria-label="Notepad">
    <svg class="curve" viewBox="0 0 100 100" preserveAspectRatio="none" aria-hidden="true">
      <path d="M0,100 L0,86 C42,84 80,66 100,30 L100,100 Z"/>
    </svg>
    <div class="rings" aria-hidden="true">
      <span></span><span></span><span></span><span></span><span></span><span></span><span></span><span></span><span></span><span></span><span></span><span></span><span></span><span></span><span></span><span></span><span></span><span></span><span></span><span></span>
    </div>
    <div class="faint-name" aria-hidden="true">NORVATH</div>
    <div class="details">
      <div class="company">NORVATH LIMITED</div>
      <div>w: www.norvathdigital.example &nbsp;|&nbsp; e: info@norvathdigital.example</div>
      <div>t: 01632 960 417</div>
      <div>48 Tamsin Lane Loughborough Leicestershire LE11 9QX</div>
      <div>Company Number: 20473915</div>
    </div>
  </section>

  <!-- Business card, front -->
  <section class="sheet card card-front" aria-label="Business card front">
    <svg class="curve" viewBox="0 0 100 100" preserveAspectRatio="none" aria-hidden="true">
      <path d="M0,100 L0,32 C40,34 80,28 100,14 L100,100 Z"/>
    </svg>
    <div class="brand"><span class="dot"></span>NORVATH</div>
    <div class="person">
      <div class="name">ELIAS MARLOW</div>
      <div class="role">Creative Director</div>
      <div class="company">NORVATH LIMITED</div>
      <div>t: 01632 960 417</div>
      <div>e: info@norvathdigital.example</div>
      <div>w: www.norvathdigital.example</div>
      <div>48 Tamsin Lane Loughborough</div>
      <div>Leicestershire LE11 9QX</div>
      <div>Company Number: 20473915</div>
    </div>
  </section>

  <!-- Business card, back -->
  <section class="sheet card card-back" aria-label="Business card back">
    <div class="brand"><span class="dot"></span>NORVATH</div>
  </section>

  <!-- Envelope -->
  <section class="sheet envelope" aria-label="Envelope">
    <svg class="curve" viewBox="0 0 100 100" preserveAspectRatio="none" aria-hidden="true">
      <path d="M0,0 L100,0 C92,40 60,65 0,78 Z"/>
    </svg>
    <div class="brand"><span class="dot"></span>NORVATH</div>
    <div class="details">
      <div class="company">NORVATH LIMITED</div>
      <div>w: www.norvathdigital.example &nbsp;|&nbsp; t: 01632 960 417</div>
      <div>48 Tamsin Lane Loughborough LE11 9QX</div>
    </div>
  </section>

  <!-- Pens -->
  <div class="pen" style="top:622px" aria-label="Branded pen">
    <span class="tip"></span><span class="clip"></span>
    <span class="grip">www.norvathdigital.example</span>
  </div>
  <div class="pen" style="top:672px" aria-label="Branded pen">
    <span class="tip"></span><span class="clip"></span>
    <span class="grip">www.norvathdigital.example</span>
  </div>
  <div class="pen" style="top:722px" aria-label="Branded pen">
    <span class="tip"></span><span class="clip"></span>
    <span class="grip">www.norvathdigital.example</span>
  </div>

</body>
</html>
```